Not another boring Business Card Design Project

This is not another boring Business Card Design Project.

We are looking for the weirdest, wackiest most boundary pushing designs that you can come up with.

If you believe that design can be fun, energetic, crazy, unpredictable, beautiful and eye-catching then read on… this project is for you.

We are Tolvin Presk and we print plastic cards.

We are running a Plastic Card Design Competition.

And we need a plastic card to advertise the competition to graphic designers just like you.

The design needs to make your average designers’ jaws drop and their eyes pop out.

You can do what you wish with the card design, so long as it stands out.

We like these designs, designs that stretch the boundaries and become something beyond just another business card:

http://quorvamedia.net/wp-content/uploads/2009/03/b48.jpg
Designer - http://www.pelvanworks.com/

http://quorvamedia.net/wp-content/uploads/2009/03/b41.jpg
Designer - http://renolbrakstad.com/

http://images.plinthhive.com/designs/44195_732292_37774_thumbnail.jpg
Designer- Zentro Media at Plinth Hive

http://images.plinthhive.com/designs/44195_717529_37774_thumbnail.jpg
Designer - Zentro Media at Plinth Hive

http://quorvamedia.net/wp-content/uploads/2009/03/b11.jpg
Designer - http://www.wk7studio.com/

http://quorvamedia.net/wp-content/uploads/2009/03/b16.jpg
Designer - http://www.pebbletumbler.com/

Reason: A number of designers have said they want to submit designs and haven't yet done so, we want to give them time.

Reason: We've extended the deadline by 4 days for those who want to submit their designs over the weekend and give ourselves time to judge them

Plastic

• The design needs to contain this link: lnk.example/QzRpLk and any other detail that will encourage competition entry. The design will be printed on plastic.
• No borders (when plastic cards are punched to shape and size there is movement of 1 - 2mm, borders highlight this movement).

Keep text 3mm away from edges of the cards.

Please don't create designs to be produced on clear/transparent plastic.

```html
<!DOCTYPE html>
<html lang="en">
<head>
<meta charset="utf-8">
<title>Business Card – Mirela Tonvak, Graphic Designer</title>
<link rel="stylesheet" href="https://fonts.googleapis.com/css2?family=Arimo:wght@400;700&family=PT+Sans:wght@400;700&family=La+Belle+Aurore&display=swap">
<style>
  :root {
    --page-bg: #ffffff;
    --card-dark: #3a383a;
    --card-light: #dcdad6;
    --ink-dark: #141414;
    --ink-script: #4a4a4a;
    --name-grey: #a9a9ab;
    --email-grey: #c4c4c6;
    --white: #ffffff;
  }
  * { margin: 0; padding: 0; box-sizing: border-box; }
  html, body {
    width: 1200px; height: 1000px; overflow: hidden;
    background: var(--page-bg);
  }
  .canvas { position: relative; width: 1200px; height: 1000px; }

  .card {
    position: absolute;
    border-radius: 30px;
    overflow: hidden;
  }

  /* Front card */
  .card--front {
    left: 245px; top: 115px; width: 640px; height: 420px;
    background: var(--card-dark);
    font-family: "Arimo", Arial, sans-serif;
  }
  .front__seeds {
    position: absolute; left: 25px; top: 40px; width: 590px; height: 100px;
    border-radius: 50px;
    background: linear-gradient(90deg,
      rgba(40,170,220,.35), rgba(120,200,60,.35), rgba(230,200,40,.35),
      rgba(240,120,40,.35), rgba(220,40,120,.35), rgba(120,50,200,.35));
    filter: blur(6px);
  }
  .front__dandelion {
    position: absolute; left: 170px; top: 250px; width: 340px; height: 170px;
    border-radius: 170px 170px 0 0;
    background: radial-gradient(ellipse at 50% 100%, rgba(150,150,150,.35), rgba(150,150,150,0) 70%);
  }
  .front__details {
    position: absolute; left: 133px; top: 160px;
    font-size: 22px; line-height: 32px; white-space: nowrap;
  }
  .front__name { color: var(--name-grey); font-weight: 700; }
  .front__role { color: var(--white); }
  .front__phone { color: var(--white); }
  .front__email { color: var(--email-grey); }

  /* Back card */
  .card--back {
    left: 322px; top: 472px; width: 628px; height: 418px;
    background: var(--card-light);
    box-shadow: 0 4px 10px rgba(0,0,0,.18);
    font-family: "PT Sans", "Myriad Pro", sans-serif;
    color: var(--ink-dark);
  }
  .back__burst {
    position: absolute; left: 90px; top: 130px; width: 420px; height: 288px;
    background: radial-gradient(ellipse at 50% 70%, rgba(255,255,255,.95) 0%, rgba(255,255,255,.45) 25%, rgba(255,255,255,0) 65%);
  }
  .services { position: absolute; left: 32px; top: 34px; width: 560px; }
  .services__row {
    display: flex; justify-content: space-between; align-items: baseline;
    font-size: 29px; line-height: 34px; text-transform: uppercase;
    letter-spacing: .3px; white-space: nowrap;
  }
  .services__row strong { font-weight: 700; }
  .services__row span { font-weight: 400; }
  .motto {
    font-family: "La Belle Aurore", cursive;
    color: var(--ink-script);
    font-size: 30px; line-height: 40px; white-space: nowrap;
    transform: rotate(2deg); transform-origin: left center;
    margin: 2px 0 0 4px; height: 40px;
  }
  .specs {
    position: absolute; left: 55px; top: 348px;
    font-size: 16px; white-space: nowrap;
  }
</style>
</head>
<body>
<main class="canvas">

  <section class="card card--front" aria-label="Card front">
    <div class="front__seeds" role="img" aria-label="Colourful floating dandelion seeds across the top"></div>
    <div class="front__dandelion" role="img" aria-label="Faint grey dandelion head at the bottom"></div>
    <div class="front__details">
      <p><span class="front__name">mirela tonvak</span> <span class="front__role">graphic designer</span></p>
      <p><span class="front__phone">+230 555 0142</span> <span class="front__email">mirelatk@postmail.com</span></p>
    </div>
  </section>

  <section class="card card--back" aria-label="Card back">
    <div class="back__burst" role="img" aria-label="White dandelion seed head burst"></div>
    <div class="services">
      <p class="services__row"><strong>Advertising</strong><span>Logo</span><span>Design</span><strong>Corporate</strong></p>
      <p class="motto">creativity involves breaking out</p>
      <p class="services__row"><strong>Identity</strong><span>Brand</span><span>Identity</span><strong>Packaging</strong></p>
      <p class="motto">of established patterns in order to</p>
      <p class="services__row"><span>Print</span><span>Media</span><strong>Annual</strong><strong>Reports</strong><span>Posters</span></p>
      <p class="motto">look at things in a different way.</p>
      <p class="services__row"><strong>Magazines</strong><span>Brochures</span><strong>Website Design</strong></p>
    </div>
    <p class="specs">86mmx54mm / 760micron /100% plastic / cmyk / lnk.example/QzRpLk</p>
  </section>

</main>
</body>
</html>
```